" Empresa privada voltada a prestação de serviços nos ramos do direito Administrativo, Previdenciário, Tributário e Municipal, para particulares e pessoas jurídicas de direito público. "

```html
<!DOCTYPE html>
<html lang="pt-BR">
<head>
<meta charset="utf-8">
<title>Moraes &amp; Lima — Envelopes</title>
<link href="https://fonts.googleapis.com/css2?family=Cormorant+Garamond:wght@500&family=Montserrat:wght@400&display=swap" rel="stylesheet">
<style>
  :root{
    --page:#ecebe8;
    --envelope-top:#9a9a9a;
    --envelope-bottom:#858585;
    --flap:#f7f7f7;
    --ink:#ffffff;
    --ink-soft:rgba(255,255,255,.8);
    --mark-faint:rgba(255,255,255,.12);
  }
  *{margin:0;padding:0;box-sizing:border-box}
  html,body{width:1200px;height:1200px;overflow:hidden;background:var(--page)}
  .sheet{position:relative;width:1200px;height:1200px;display:flex;justify-content:center;align-items:center;gap:80px}
  .envelope{position:relative;width:440px;height:620px}
  .envelope-shape{position:absolute;inset:0}
  .envelope-body{position:absolute;left:0;right:0;top:40px;bottom:0;background:linear-gradient(160deg,var(--envelope-top),var(--envelope-bottom));box-shadow:0 10px 24px rgba(0,0,0,.15)}
  .faint-mark{position:absolute;left:170px;top:150px;width:110px;height:110px;border:3px solid var(--mark-faint)}
  .brand{position:absolute;left:40px;bottom:62px;right:40px;color:var(--ink)}
  .brand-row{display:flex;align-items:center;gap:10px}
  .brand-square{width:20px;height:20px;border:1.5px solid var(--ink)}
  .brand-name{font-family:"Cormorant Garamond",serif;font-weight:500;font-size:22px;letter-spacing:.14em;text-transform:uppercase}
  .brand-tagline{font-family:"Montserrat",sans-serif;font-size:7px;letter-spacing:.3em;text-transform:uppercase;color:var(--ink-soft);margin:4px 0 0 30px}
  .brand-rule{margin-top:14px;height:1px;background:var(--ink-soft)}
  .contact{position:absolute;left:40px;bottom:150px;font-family:"Montserrat",sans-serif;font-size:8px;line-height:1.7;color:var(--ink-soft)}
</style>
</head>
<body>
<main class="sheet">

  <section class="envelope envelope-front">
    <svg class="envelope-shape" width="440" height="620" viewBox="0 0 440 620" aria-hidden="true">
      <path d="M0 40 L20 4 Q22 0 28 0 L412 0 Q418 0 420 4 L440 40 Z" fill="var(--flap)"/>
    </svg>
    <div class="envelope-body">
      <div class="brand">
        <div class="brand-row"><span class="brand-square"></span><span class="brand-name">Moraes &amp; Lima</span></div>
        <p class="brand-tagline">Advocacia e Consultoria</p>
        <div class="brand-rule"></div>
      </div>
    </div>
  </section>

  <section class="envelope envelope-back">
    <svg class="envelope-shape" width="440" height="620" viewBox="0 0 440 620" aria-hidden="true">
      <path d="M0 40 L20 4 Q22 0 28 0 L412 0 Q418 0 420 4 L440 40 Z" fill="var(--flap)"/>
    </svg>
    <div class="envelope-body">
      <div class="faint-mark"></div>
      <address class="contact">
        Rua das Acácias, 210 – Sala 5<br>
        Centro – Campinas / SP<br>
        (19) 3200-4100<br>
        contato@moraeslima.adv.br
      </address>
      <div class="brand">
        <div class="brand-row"><span class="brand-square"></span><span class="brand-name">Moraes &amp; Lima</span></div>
        <p class="brand-tagline">Advocacia e Consultoria</p>
        <div class="brand-rule"></div>
      </div>
    </div>
  </section>

</main>
</body>
</html>
```